PRESENTATION FOLDER DESIGN

I would like to design a presentation folder that is 6 x 9 with 2 x 4 inch pockets.
I have attached the logo to use as well as the template for the presentation folder.

I also included the front and back of the business cards so that you can see the overall look I am trying to go for as well as the information to have on there.

The presentation folder will be used to send out an invitation to a conference for dentists.

Target Market(s)

dentists

Font styles to use
Sans Serif

Requirements
Must have
• The clours must be the same as on the logo.
• On the cover, I would like a title in bold large letters that says:
• PLEASE JOIN US FOR OUR EXCLUSIVE EVENTS
• FOR DENTAL PROFESSIONALS
• *eligible for CE credits
• I would like to have this picture on the cover as well.
• ON THE BACK, i WOULD THE COLOURS TO BE THE BLUE FROM THE LOGO AND THE WRITING IN WHITE.
• THE INSIDE FLAPS MUST BE IN THE BLUE BUT THE INSIDE OF THE FOLDER SHOULD BE IN ORANGE.
• ON THE INSIDE FLAPS WE SHOULD WRITE:
• ON THE LEFT FLAP: I WANT TO PURCHASE A CLINIC
• ON THE RIGHT FLAP: I WANT TO SELL MY CLINIC

```html
<!DOCTYPE html>
<html lang="en">
<head>
<meta charset="utf-8">
<title>Dentivest Presentation Folder – Outside</title>
<link href="https://fonts.googleapis.com/css2?family=Questrial&family=Lato:wght@400;700;900&display=swap" rel="stylesheet">
<style>
  :root {
    --brand-blue: #2bbfd6;
    --brand-blue-deep: #23b0c8;
    --brand-orange: #f26a2a;
    --paper: #ffffff;
    --paper-shade: #e4e6e7;
    --backdrop: #4d4f4c;
    --ink-white: #ffffff;
  }
  * { box-sizing: border-box; margin: 0; padding: 0; }
  html, body { width: 1200px; height: 929px; overflow: hidden; background: var(--backdrop); }
  .folder {
    position: absolute; left: 20px; top: 30px;
    width: 1160px; height: 869px;
    display: flex;
    box-shadow: 6px 8px 14px rgba(0,0,0,.45);
  }
  /* Back panel */
  .back {
    position: relative; width: 580px; height: 100%;
    background: linear-gradient(160deg, var(--brand-blue) 0%, var(--brand-blue) 60%, var(--brand-blue-deep) 100%);
    color: var(--ink-white);
  }
  .back__services {
    position: absolute; top: 60px; left: 0; width: 100%;
    text-align: center; font: 15px/1 "Questrial", sans-serif; letter-spacing: .1px;
  }
  .back__intro {
    position: absolute; top: 94px; left: 50px; width: 480px;
    font: 11.2px/1.35 "Lato", sans-serif; text-align: justify; text-align-last: center;
  }
  .back__intro strong { font-weight: 700; }
  .back__name {
    position: absolute; top: 395px; left: 0; width: 100%;
    text-align: center; font: 52px/1 "Questrial", sans-serif; letter-spacing: 2px;
  }
  .back__company { position: absolute; left: 50px; top: 783px; font: 12px/1.3 "Lato", sans-serif; }
  .back__company h2 { font: 700 16px/1.1 "Lato", sans-serif; }
  .back__contact {
    position: absolute; right: 50px; top: 786px; list-style: none;
    font: 12px/1.28 "Lato", sans-serif; text-align: right;
  }
  .back__contact li { display: flex; justify-content: flex-end; align-items: center; gap: 6px; }
  .back__contact svg { width: 11px; height: 11px; }

  /* Front cover */
  .cover {
    position: relative; width: 580px; height: 100%;
    background: linear-gradient(90deg, var(--paper-shade) 0%, var(--paper) 32%, var(--paper) 100%);
  }
  .cover__title {
    position: absolute; top: 52px; left: 0; width: 100%; text-align: center;
    font: 66px/1 "Questrial", sans-serif; color: var(--brand-orange); letter-spacing: 1px;
  }
  .cover__subtitle {
    position: absolute; top: 114px; left: 0; width: 100%; text-align: center;
    font: 900 34px/1 "Lato", sans-serif; color: var(--brand-blue); letter-spacing: 1px;
  }
  .stripe { position: absolute; left: 0; width: 100%; height: 12px; }
  .stripe--top { top: 192px; background: linear-gradient(90deg, var(--brand-blue) 60%, var(--brand-orange) 60%); }
  .stripe--bottom { top: 583px; background: linear-gradient(90deg, var(--brand-orange) 56%, var(--brand-blue) 56%); }
  .cover__photo {
    position: absolute; top: 204px; left: 0; width: 100%; height: 379px;
    background: linear-gradient(135deg, #f2f6f6 0%, #dfe9ea 40%, #9fd8e2 70%, #cfe0d4 100%);
  }
  .cover__name {
    position: absolute; top: 636px; left: 0; width: 100%; text-align: center;
    font: 56px/1 "Questrial", sans-serif; color: var(--brand-blue); letter-spacing: 1px;
  }
  .cover__audience {
    position: absolute; top: 748px; left: 0; width: 100%; text-align: center;
    font: 34px/1 "Questrial", sans-serif; color: var(--brand-blue);
  }
  .cover__note {
    position: absolute; top: 784px; left: 58px; width: 468px;
    display: flex; align-items: center; gap: 10px;
    font: 22px/1 "Questrial", sans-serif; color: var(--brand-orange); white-space: nowrap;
  }
  .cover__note .rule { flex: 1; height: 1.5px; background: var(--brand-orange); position: relative; }
  .cover__note .rule::after {
    content: ""; position: absolute; top: -2px; width: 5px; height: 5px; border-radius: 50%;
    background: var(--brand-orange);
  }
  .cover__note .rule--left::after { right: 0; }
  .cover__note .rule--right::after { left: 0; }
</style>
</head>
<body>
  <main class="folder">
    <section class="back">
      <p class="back__services">BUSINESS LAW | TAXATION | INCORPORATION OF PROFESSIONALS</p>
      <p class="back__intro"><strong>DENTIVEST</strong> is a boutique law and tax firm devoted to offering advanced legal and tax planning strategies in order to optimize the corporate structure of a dental practice as well as the purchase and sale of practice, working with both buyers and sellers.</p>
      <p class="back__name">DENTIVEST</p>
      <address class="back__company" style="font-style:normal">
        <h2>DENTIVEST ADVISORY INC.</h2>
        410-2250 rue des Érables<br>Laval (QC) H7X 1B4
      </address>
      <ul class="back__contact">
        <li>555.014.2288
          <svg viewBox="0 0 12 12"><rect x="3" y="1" width="6" height="10" rx="1" fill="none" stroke="#fff" stroke-width="1.2"/></svg></li>
        <li>events@dentivest.ca
          <svg viewBox="0 0 12 12"><rect x="1" y="2.5" width="10" height="7" fill="#fff"/><path d="M1 2.5 6 6.5 11 2.5" fill="none" stroke="#2bbfd6" stroke-width="1"/></svg></li>
        <li>dentivest.ca
          <svg viewBox="0 0 12 12"><circle cx="6" cy="6" r="5" fill="#fff"/><path d="M1 6h10M6 1v10" stroke="#2bbfd6" stroke-width=".8"/></svg></li>
      </ul>
    </section>

    <section class="cover">
      <h1 class="cover__title">PLEASE JOIN US</h1>
      <p class="cover__subtitle">FOR OUR EXCLUSIVE EVENTS</p>
      <div class="stripe stripe--top"></div>
      <div class="cover__photo" role="img" aria-label="Photo of a bright dental clinic with a light blue dental chair and instruments"></div>
      <div class="stripe stripe--bottom"></div>
      <p class="cover__name">DENTIVEST</p>
      <p class="cover__audience">FOR DENTAL PROFESSIONALS</p>
      <p class="cover__note"><span class="rule rule--left"></span>*eligible for CE credits<span class="rule rule--right"></span></p>
    </section>
  </main>
</body>
</html>
```